Revamp of current landing page for high conversions

I need to revamp my current landing pages and I want to see designs that incorporate elements from both of these current designs... http://www.brightmarlowsmilestudio.com/

https://qrtmno.pagewick.co/vorn-glowpackoffer77/

Please implement these images into the design: https://www.pictogram.example/p/KQX7Lm2R_Ta-/?taken-by=brightmarlowsmilestudio

https://www.pictogram.example/p/KR4WnsJdpzG/?taken-by=brightmarlowsmilestudio

https://www.pictogram.example/p/KRvqDmtk9_P/?taken-by=brightmarlowsmilestudio

https://www.pictogram.example/p/KRjemTGkRVN/?taken-by=brightmarlowsmilestudio

https://www.pictogram.example/p/KRjfa93kd-d/?taken-by=brightmarlowsmilestudio

https://www.pictogram.example/p/KReZoGTEuHa/?taken-by=brightmarlowsmilestudio

https://www.pictogram.example/p/KRThd5hkmc9/?taken-by=brightmarlowsmilestudio

https://www.pictogram.example/p/KRBksT0EcSu/?taken-by=brightmarlowsmilestudio

https://www.pictogram.example/p/KS8h5SjE8H9/?taken-by=brightmarlowsmilestudio

Target Market(s)

People that care about their looks and who want whiter teeth. People that are interested in good oral hygeine

Industry/Entity Type

Dental Clinic

Number of Pages Required

1 page

Colors

Designer to choose colors to be used in the design.

Requirements
Must have
• images of my customers that I have included in the description.
• Also, I would like to see a professional laser teeth whitening treatment that happens in dental office and make emphasis on FREE HOME MAINTENANCE KIT INCLUDED!
• Must have CALL OR TEXT 555-014-3827
Nice to have
• Must be mobile friendly responsive design-use logo from my website www.brightmarlowsmilestudo.com
Should not have
• stock images of people I dont like stock images of people so please use the images from my instagram account

```html
<!DOCTYPE html>
<html lang="en">
<head>
<meta charset="utf-8">
<title>Bright Marlow Smile Studio — $99 Teeth Whitening</title>
<link href="https://fonts.googleapis.com/css2?family=Lato:ital,wght@0,300;0,400;0,700;0,900;1,300;1,400;1,700&display=swap" rel="stylesheet">
<style>
:root{
  --blue:#1b87c9;
  --blue-light:#3ab4ec;
  --navy:#0e4f7a;
  --navy-deep:#0b4368;
  --orange:#f39200;
  --orange-dark:#c76f00;
  --green:#8dc63f;
  --teal:#2bb7a0;
  --ink:#333;
  --grey:#8a8f94;
  --pale:#f5fafd;
  --white:#fff;
}
*{box-sizing:border-box;margin:0;padding:0}
html,body{width:1200px;height:2267px;overflow:hidden;background:var(--white);font-family:'Lato',sans-serif;color:var(--ink)}
.page{position:relative;width:1200px;height:2267px}
section,header,footer{position:relative;width:1200px}
.abs{position:absolute}

/* header */
.site-header{height:104px;background:var(--white)}
.brand{left:132px;top:22px;display:flex;align-items:center;gap:12px}
.brand-dot{width:58px;height:58px;border-radius:50%;background:#d9e3ea}
.brand-name{font-size:24px;font-weight:700;color:var(--blue);line-height:1}
.contact{right:132px;top:32px;text-align:right}
.contact-label{font-size:14px;color:var(--grey);letter-spacing:1px;border-bottom:1px solid var(--grey);padding-bottom:2px}
.contact-phone{font-size:21px;color:var(--blue-light);font-weight:400}

/* photo strips */
.photo-strip{display:flex}
.photo-strip .shot{flex:1;height:100%}
.strip-top{height:103px}
.strip-bottom{height:144px}
.shot.a{background:linear-gradient(180deg,#c9c3bf,#7a3646)}
.shot.b{background:linear-gradient(180deg,#d4d0cc,#3f6f8c)}
.shot.c{background:linear-gradient(180deg,#cfc9c6,#6b3a4a)}
.shot.d{background:linear-gradient(180deg,#d8d4d0,#2d2f35)}

/* hero */
.hero{height:387px;background:var(--blue);color:var(--white)}
.hero-title{left:133px;top:42px;font-size:29px;font-style:italic;font-weight:300}
.hero-for{left:133px;top:92px;font-size:29px;font-style:italic;font-weight:300}
.ribbon{position:absolute}
.ribbon-price{position:absolute;left:0;right:0;text-align:center;font-weight:900;color:var(--white)}
.hero-ribbon{left:288px;top:70px;width:285px;height:100px}
.hero-ribbon .ribbon-price{top:6px;font-size:72px;line-height:1}
.benefits{top:192px;font-size:14px;font-style:italic;list-style:none;line-height:20px}
.benefits li{display:flex;align-items:center;gap:9px}
.benefits.col1{left:155px}
.benefits.col2{left:372px}
.extras{left:132px;top:270px;list-style:none;font-size:19px;font-weight:700;line-height:32px}
.extras li{display:flex;align-items:center;gap:12px}
.extras .plus{color:var(--green);font-size:24px;font-weight:700}
.offer-tag{left:647px;top:104px;width:128px;height:62px;background:var(--blue-light);text-align:center;color:var(--white);padding-top:6px}
.offer-tag small{display:block;font-size:14px}
.offer-tag strong{display:block;font-size:29px;font-weight:900;line-height:1.05}
.coupon-box{left:772px;top:37px;width:296px;height:293px;background:var(--navy);box-shadow:0 4px 10px rgba(0,0,0,.25);text-align:center}
.coupon-intro{margin-top:14px;font-size:13px;font-style:italic;line-height:17px}
.coupon-title{margin-top:8px;font-size:19px;font-style:italic}
.coupon-rule{margin:16px 0 0;border-top:1px dashed rgba(255,255,255,.6)}
.field{display:block;width:200px;height:30px;margin:0 auto;background:var(--white);color:#b5b5b5;font-size:13px;text-align:left;padding:7px 8px}
.coupon-fields{margin-top:24px;display:flex;flex-direction:column;gap:13px}
.cta{display:inline-block;background:var(--orange);color:var(--white);font-weight:700;font-size:15px;border-radius:20px;width:152px;height:40px;line-height:40px;box-shadow:0 3px 5px rgba(0,0,0,.25)}
.coupon-box .cta{margin-top:34px}

/* intro */
.intro{height:132px;text-align:center;padding-top:38px;font-size:19px;line-height:29px;color:#555;font-weight:300}
.intro strong{font-weight:700;color:var(--ink)}

/* how it works */
.how{height:323px;background:var(--pale)}
.section-heading{font-size:19px;font-weight:700;color:var(--blue)}
.how .section-heading{left:133px;top:72px}
.how-text{left:133px;top:120px;width:370px;font-size:13.5px;line-height:22px;color:#a0a4a8;font-weight:300}
.team-photo{left:510px;top:60px;width:575px;height:263px;background:radial-gradient(ellipse at 50% 70%,#c9a692 0%,#7a3a48 45%,rgba(245,250,253,0) 75%)}
.review-badge{left:975px;top:38px;width:90px;height:90px;border-radius:50%;background:#d52b2b}
.review-strip{left:980px;top:133px;width:80px;height:12px;background:#d52b2b}

/* testimonial */
.testimonial{height:408px;background:var(--blue);color:var(--white)}
.quote-mark{left:126px;top:86px;font-size:56px;font-weight:900;line-height:1}
.quote-text{left:205px;top:98px;width:395px;font-size:14.5px;line-height:24px}
.quote-author{left:205px;top:298px;font-size:14.5px}
.quote-author b{font-weight:700}
.quote-author span{color:#cfe6f5;font-weight:300}
.deal{left:730px;top:58px;width:330px;text-align:center}
.deal-kicker{font-size:14px;color:#d9ecf8;line-height:18px}
.deal-for{font-size:28px;font-weight:700;margin-top:2px}
.deal-ribbon{position:relative;width:330px;height:100px;margin-top:4px}
.deal-ribbon .ribbon-price{top:4px;font-size:78px;line-height:1}
.deal-save{font-size:13px;font-style:italic;line-height:16px;margin-top:-4px}
.deal-best{font-size:15px;font-weight:700;margin-top:14px}
.deal-occasions{font-size:14px;color:#a9d1ec;line-height:18px;margin-top:6px}

/* features */
.features{height:430px;background:var(--pale)}
.features .section-heading{left:133px;top:74px}
.feat-icon{position:absolute;top:70px;width:40px;height:40px;margin-left:-20px}
.feat-label{position:absolute;top:128px;width:160px;margin-left:-80px;text-align:center;font-size:13.5px;font-style:italic;color:#555}
.compare{position:absolute;left:130px;top:174px;width:940px;border-collapse:collapse;font-size:13.5px;color:#666}
.compare td{height:49px;text-align:center;width:160px;border-bottom:1px solid #e3e8ec}
.compare td:first-child{text-align:left;width:140px;font-weight:700;font-style:italic;color:#222}
.compare tr.ours td{color:var(--blue);font-weight:700;font-size:14.5px;border-bottom:1px solid #e3e8ec}
.compare tr:last-child td{border-bottom:none}
.table-brand{display:flex;align-items:center;gap:5px;font-style:normal;font-size:10px;color:var(--blue)}
.table-brand i{width:18px;height:18px;border-radius:50%;background:#d9e3ea;display:inline-block}

/* footer signup */
.signup{height:236px;background:var(--navy-deep);color:var(--white);text-align:center}
.signup-intro{padding-top:26px;font-size:14px;font-style:italic}
.signup-title{font-size:28px;font-style:italic;margin-top:4px}
.signup-rule{position:absolute;left:0;width:1200px;border-top:1px dashed rgba(255,255,255,.45)}
.signup-form{left:133px;top:139px;display:flex;gap:25px}
.signup-form .field{width:215px;margin:0}
.signup-form .cta{border-radius:0;width:215px;height:30px;line-height:30px;font-size:15px}
.copyright{left:0;right:0;top:204px;text-align:center;font-size:10px;color:#86a8c0}
</style>
</head>
<body>
<div class="page">

  <header class="site-header">
    <div class="abs brand"><span class="brand-dot"></span><span class="brand-name">Bright Marlow Smile Studio</span></div>
    <div class="abs contact">
      <div class="contact-label">CALL OR TEXT</div>
      <div class="contact-phone">555-014-3827</div>
    </div>
  </header>

  <div class="photo-strip strip-top" role="img" aria-label="Row of customer photos with clinic staff holding smile signs">
    <div class="shot a"></div><div class="shot b"></div><div class="shot c"></div><div class="shot d"></div><div class="shot a"></div><div class="shot c"></div>
  </div>

  <section class="hero">
    <div class="abs hero-title">$378 Teeth Whitening System</div>
    <div class="abs hero-for">For Only</div>
    <div class="ribbon hero-ribbon">
      <svg width="285" height="100" viewBox="0 0 285 100">
        <polygon points="0,25 45,25 45,85 0,85 18,55" fill="var(--orange-dark)"/>
        <polygon points="285,25 240,25 240,85 285,85 267,55" fill="var(--orange-dark)"/>
        <polygon points="35,8 250,8 250,78 142,92 35,78" fill="var(--orange)"/>
      </svg>
      <div class="ribbon-price">$99</div>
    </div>
    <ul class="abs benefits col1">
      <li><svg width="12" height="10" viewBox="0 0 12 10"><path d="M1 5l3.5 3.5L11 1" stroke="var(--green)" stroke-width="2.4" fill="none"/></svg>No Pain - No Sensitivity</li>
      <li><svg width="12" height="10" viewBox="0 0 12 10"><path d="M1 5l3.5 3.5L11 1" stroke="var(--green)" stroke-width="2.4" fill="none"/></svg>Cosmetic Procedure</li>
      <li><svg width="12" height="10" viewBox="0 0 12 10"><path d="M1 5l3.5 3.5L11 1" stroke="var(--green)" stroke-width="2.4" fill="none"/></svg>Results Less Than An Hour</li>
    </ul>
    <ul class="abs benefits col2">
      <li><svg width="12" height="10" viewBox="0 0 12 10"><path d="M1 5l3.5 3.5L11 1" stroke="var(--green)" stroke-width="2.4" fill="none"/></svg>Blue Laser Technology</li>
      <li><svg width="12" height="10" viewBox="0 0 12 10"><path d="M1 5l3.5 3.5L11 1" stroke="var(--green)" stroke-width="2.4" fill="none"/></svg>2-8 Shades Lighter</li>
      <li><svg width="12" height="10" viewBox="0 0 12 10"><path d="M1 5l3.5 3.5L11 1" stroke="var(--green)" stroke-width="2.4" fill="none"/></svg>Convenient Location in San Diego</li>
    </ul>
    <ul class="abs extras">
      <li><span class="plus">+</span>Free Home Maintenance Kit Included!</li>
      <li><span class="plus">+</span>1 In Office Teeth Whitening Treatment 45 Minutes</li>
    </ul>
    <div class="abs offer-tag"><small>Limited Time</small><strong>OFFER</strong></div>
    <div class="abs coupon-box">
      <div class="coupon-intro">Enter your info<br>to be emailed the $99</div>
      <div class="coupon-title">Teeth Whitening Coupon</div>
      <div class="coupon-rule"></div>
      <div class="coupon-fields">
        <span class="field">Name</span>
        <span class="field">Email</span>
        <span class="field">Phone</span>
      </div>
      <span class="cta">Get A Deal!</span>
    </div>
  </section>

  <div class="photo-strip strip-bottom" role="img" aria-label="Second row of customer photos with smiling clients and staff">
    <div class="shot d"></div><div class="shot c"></div><div class="shot b"></div><div class="shot a"></div><div class="shot c"></div><div class="shot b"></div><div class="shot a"></div>
  </div>

  <section class="intro">
    <p><strong>Why pay hundreds of dollars</strong> when you can get a professional teeth whitening<br>procedure for much less than your local dentist office?</p>
  </section>

  <section class="how">
    <h2 class="abs section-heading">How It Works</h2>
    <p class="abs how-text">We utilize the latest Blue Light Whitening Technology in combination with our Hydrogen Peroxide Whitening Gel to accelerate the whitening process! It's effective, safe and affordable! With our treatment your smile will be noticeably whiter in less than an hour!</p>
    <div class="abs team-photo" role="img" aria-label="Photo of a smiling client standing between two clinic staff members"></div>
    <div class="abs review-badge" role="img" aria-label="Review rating badge"></div>
    <div class="abs review-strip"></div>
  </section>

  <section class="testimonial">
    <div class="abs quote-mark">&ldquo;</div>
    <p class="abs quote-text">So I just had my teeth whitened using the blue laser light and I have to say this was one of the best experiences I've had with teeth whitening. Marisol (the women who helped me) was very clear about the process and walked me through each ste. I would say the whole process took about 45-60 minutes. After the teeth whitening process was finished I could tell immediately and I was very pleased with the end results.</p>
    <p class="abs quote-author"><b>Dario V.</b> <span>San Diego, CA</span></p>
    <div class="abs deal">
      <div class="deal-kicker">Affordable Teeth Whitening<br>in San Diego</div>
      <div class="deal-for">for only</div>
      <div class="ribbon deal-ribbon">
        <svg width="330" height="100" viewBox="0 0 330 100">
          <polygon points="0,28 55,28 55,88 0,88 20,58" fill="var(--orange-dark)"/>
          <polygon points="330,28 275,28 275,88 330,88 310,58" fill="var(--orange)"/>
          <polygon points="42,8 288,8 288,82 165,96 42,82" fill="var(--orange)"/>
        </svg>
        <div class="ribbon-price">$99</div>
      </div>
      <div class="deal-save">Save Hundreds vs<br>Going To Your Local Dentist!</div>
      <div class="deal-best">The best price, service and results</div>
      <div class="deal-occasions">Get ready for High School Prom, Mother's Day,<br>Graduation, Wedding, Vacation, or any Occasion.</div>
    </div>
  </section>

  <section class="features">
    <h2 class="abs section-heading">Features</h2>
    <svg class="feat-icon" style="left:360px" viewBox="0 0 40 40"><circle cx="20" cy="20" r="17" fill="none" stroke="var(--teal)" stroke-width="2"/><path d="M20 22l8-9" stroke="var(--teal)" stroke-width="2"/><path d="M8 20h3M29 20h3M20 8v3" stroke="var(--teal)" stroke-width="2"/></svg>
    <svg class="feat-icon" style="left:520px" viewBox="0 0 40 40"><circle cx="20" cy="20" r="6" fill="none" stroke="var(--teal)" stroke-width="2"/><circle cx="20" cy="20" r="13" fill="none" stroke="var(--teal)" stroke-width="2" stroke-dasharray="5 3.2"/></svg>
    <svg class="feat-icon" style="left:680px" viewBox="0 0 40 40"><rect x="5" y="10" width="30" height="22" rx="2" fill="none" stroke="var(--teal)" stroke-width="2"/><path d="M5 15l24-8v3" fill="none" stroke="var(--teal)" stroke-width="2"/><rect x="24" y="18" width="11" height="7" fill="none" stroke="var(--teal)" stroke-width="2"/></svg>
    <svg class="feat-icon" style="left:840px" viewBox="0 0 40 40"><circle cx="20" cy="20" r="17" fill="none" stroke="var(--teal)" stroke-width="2"/><path d="M20 9v11l7 5" fill="none" stroke="var(--teal)" stroke-width="2"/></svg>
    <svg class="feat-icon" style="left:1000px" viewBox="0 0 40 40"><path d="M28 7H7v28h24V16" fill="none" stroke="var(--teal)" stroke-width="2"/><path d="M34 6l-14 14-2 5 5-2 14-14z" fill="none" stroke="var(--teal)" stroke-width="2"/></svg>
    <span class="feat-label" style="left:360px">Speed</span>
    <span class="feat-label" style="left:520px">Ease of Use</span>
    <span class="feat-label" style="left:680px">Cost</span>
    <span class="feat-label" style="left:840px">Time Requirements</span>
    <span class="feat-label" style="left:1000px">Availability</span>
    <table class="compare">
      <tr class="ours"><td><span class="table-brand"><i></i>Bright Marlow</span></td><td>Results in 45 minutes</td><td>Very Easy</td><td>$378</td><td>Less Than An Hour</td><td>Walk-In &amp; By Appt</td></tr>
      <tr><td>LUMAGLOW</td><td>Results in 3 Treatments</td><td>Difficult/Dentist</td><td>$600-$1000</td><td>3 Hours</td><td>By Appointment Only</td></tr>
      <tr><td>GLEAMLINE</td><td>Results in 1 Hour</td><td>Difficult/Dentist</td><td>$399-$600</td><td>1 Hour + Home<br>Treatment</td><td>By Appointment Only</td></tr>
      <tr><td>OTHER</td><td>7-10 Days</td><td>Self</td><td>$50-$150</td><td>Nightly 7-30 Days</td><td>Store Purchase</td></tr>
    </table>
  </section>

  <footer class="signup">
    <div class="signup-intro">Enter your info to be emailed the $99</div>
    <div class="signup-title">Teeth Whitening Coupon</div>
    <div class="signup-rule" style="top:108px"></div>
    <div class="abs signup-form">
      <span class="field">Name</span>
      <span class="field">Email</span>
      <span class="field">Phone</span>
      <span class="cta">Get A Deal!</span>
    </div>
    <div class="signup-rule" style="top:194px"></div>
    <div class="abs copyright">&copy; 2011-2016 Bright Marlow Smile Studio</div>
  </footer>

</div>
</body>
</html>
```